Online Book Sale Postcard Design

I need a postcard design to announce the online sale of my paperback book listed on Vorlenta.com and Brindlepress.com. My book is about Christmas and belief in God told in short stories, poems, and prayer to help individuals, children, and families celebrate Christmas.
I live in Houston, TX with my retired parents and younger sister in our neighborhood that has a lot of retired citizens and neighbors. The book is a tribute to the neighborhood which is the source of inspiration for the poem which has the same title as the book "Glowing Windows, Quiet Snowfall." I wrote that poem in 2001 after a car tour of the neighborhood in December of 2000.
This is my first book that I've written and is listed on Vorlenta.com and BrindlePress.com. I have a high resolution cover jpeg upload that I would like to use on the front (full color) of the postcard. The basic information showing when it's for sale and where it can be bought is what I need printed on the postcard. I have marketing copy that can be used, also. I want the postcard to convey joy and cheer to communicate the mood of the season as well as of the book, "Glowing Windows, Quiet Snowfall."
Target Market(s)
Females aged 35+, influenced by husbands and young children, teenagers, and young adults.
Industry/Entity Type
Marketing
Requirements
Nice to have
- I trust your creative judgment. Something that makes homeowners want to keep the postcard for reference and as a reminder to buy for themselves and/or give as a gift.
Should not have
- Don't crowd the postcard with too much information. Specifics is all that's needed. I trust your judgment.

```html
<!DOCTYPE html>
<html lang="en">
<head>
<meta charset="utf-8">
<title>Glowing Windows, Quiet Snowfall – Postcard</title>
<link rel="stylesheet" href="https://fonts.googleapis.com/css2?family=Parisienne&family=Great+Vibes&family=Raleway:wght@200;400&family=Open+Sans:wght@400&display=swap">
<style>
  :root {
    --gold-light: #fff3c4;
    --gold-mid: #f2c552;
    --gold-deep: #d99a1c;
    --berry-red: #b3141c;
    --deep-red: #8e1a1f;
    --title-red: #7a1a24;
    --snow: #f6f8fb;
    --cover-light: #fbf6e8;
    --cover-gold: #e6d39c;
    --author-grey: #8a6f6a;
  }
  * { margin: 0; padding: 0; box-sizing: border-box; }
  html, body { width: 1200px; height: 923px; overflow: hidden; background: #fff; }
  .postcard { position: relative; width: 1200px; height: 923px; overflow: hidden; }
  .backdrop { position: absolute; inset: 0; }

  .headline {
    position: absolute; left: 22px; top: 8px;
    font-family: "Parisienne", cursive; color: var(--deep-red);
    line-height: 1;
  }
  .headline .lead { display: block; font-size: 47px; }
  .headline .line { display: block; font-size: 33px; margin-top: 15px; }
  .headline .l1 { margin-left: 143px; }
  .headline .l2 { margin-left: 82px; }
  .headline .l3 { margin-left: 0; }
  .headline .l4 { margin-left: 55px; }
  .headline .l5 { margin-left: 95px; }

  .book { position: absolute; left: 724px; top: 92px; width: 430px; height: 670px; }
  .book-cover {
    position: absolute; left: 0; top: 8px; width: 405px; height: 662px;
    background: linear-gradient(160deg, var(--cover-light) 0%, #f3ead0 45%, var(--cover-gold) 100%);
    box-shadow: 6px 10px 18px rgba(90, 50, 0, .35);
  }
  .book-pages {
    position: absolute; left: 405px; top: 0; width: 16px; height: 662px;
    background: repeating-linear-gradient(90deg, #fff 0 2px, #e9e6df 2px 3px);
    transform: skewY(-1deg);
  }
  .cover-title { position: absolute; left: 28px; top: 100px; color: var(--title-red); line-height: .95; }
  .cover-title .script { display: block; font-family: "Great Vibes", cursive; font-size: 92px; }
  .cover-title .caps {
    display: block; font-family: "Raleway", sans-serif; font-weight: 200;
    font-size: 62px; letter-spacing: 1px; margin: 2px 0 6px 6px;
  }
  .cover-author {
    position: absolute; left: 0; right: 0; top: 590px; text-align: center;
    font-family: "Raleway", sans-serif; font-weight: 400; font-size: 19px;
    letter-spacing: 3px; color: var(--author-grey);
  }

  .availability {
    position: absolute; left: 490px; top: 770px; width: 700px;
    font-family: "Open Sans", sans-serif; color: var(--berry-red); text-align: center;
  }
  .availability .intro { font-size: 23px; color: var(--deep-red); margin-left: -90px; }
  .availability .date { font-size: 31px; color: var(--deep-red); margin-left: -70px; }
  .availability .stores { font-size: 29px; line-height: 36px; }
</style>
</head>
<body>
<main class="postcard">
  <svg class="backdrop" width="1200" height="923" viewBox="0 0 1200 923" role="img" aria-label="Golden bokeh holiday background with red berries, baubles, gold gift, bells, ribbon, pine cones and snow">
    <defs>
      <radialGradient id="goldGlow" cx="45%" cy="35%" r="80%">
        <stop offset="0" stop-color="var(--gold-light)"/>
        <stop offset=".55" stop-color="var(--gold-mid)"/>
        <stop offset="1" stop-color="var(--gold-deep)"/>
      </radialGradient>
      <radialGradient id="berryPatch" cx="25%" cy="70%" r="60%">
        <stop offset="0" stop-color="#c41a22"/>
        <stop offset=".6" stop-color="#9e1a1f"/>
        <stop offset="1" stop-color="#9e1a1f" stop-opacity="0"/>
      </radialGradient>
      <linearGradient id="snowBank" x1="0" y1="0" x2="0" y2="1">
        <stop offset="0" stop-color="#eef2f7"/>
        <stop offset="1" stop-color="var(--snow)"/>
      </linearGradient>
    </defs>
    <rect width="1200" height="923" fill="url(#goldGlow)"/>
    <ellipse cx="280" cy="720" rx="420" ry="290" fill="url(#berryPatch)"/>
    <path d="M0 900 Q300 780 620 790 Q900 800 1200 740 L1200 923 L0 923 Z" fill="url(#snowBank)"/>
  </svg>

  <h1 class="headline">
    <span class="lead">Experience the spirit of Christmas anew</span>
    <span class="line l1">through this charming collection of</span>
    <span class="line l2">holiday poetry that heralds</span>
    <span class="line l3">the Love of God,</span>
    <span class="line l4">the Comfort of Home &amp;</span>
    <span class="line l5">the Child like Joy of the Season.</span>
  </h1>

  <div class="book">
    <div class="book-pages"></div>
    <div class="book-cover">
      <h2 class="cover-title">
        <span class="script">Glowing</span>
        <span class="caps">WINDOWS,</span>
        <span class="script">Quiet</span>
        <span class="caps">SNOWFALL</span>
      </h2>
      <p class="cover-author">MARLA J. ELLISON</p>
    </div>
  </div>

  <section class="availability">
    <p class="intro">Available Online from</p>
    <p class="date">October 9, 2014&nbsp; at:</p>
    <p class="stores">www.vorlenta.com | www.brindlepress.com</p>
    <p class="stores">www.hollis&amp;reed.com</p>
  </section>
</main>
</body>
</html>
```